New Business Card Options

we need a new business card design to reflect the edgy, innovative image we want the company to portray. We also need to include the social buttons to encourage more interaction with our social media accounts.
I've attached the current business card design which is a fold out card which has lines for writing notes on the back. I'm looking for options for design as well as printing suggestions - we want to stand out and be memorable.
THE BUSINESS CARD DOES NOT HAVE TO HAVE THE PHOTO
Colours to use:
MARINE
Dark blue R000 G031 B051
Light blue R080 G177 B234
Dark blue C100 M047 Y023 K079
Light blue C083 M001 Y000 K000
Reason: I just need an extra day to shortlist designs
Reason: need more time to decide
Target Market(s)
Marine
Industry/Entity Type
Business
Contact Information for Business Card
I've attached a copy of our current business card. the new business cards may or may not include the photo - i would like options of both. I would like our social media icons adding for Twitter, Netlink, Facebook and YouTube
Font styles to use
Other font styles liked:
- Calibri
Look and feel
Each slider illustrates characteristics of the customer's brand and the style your logo design should communicate.

```html
<!DOCTYPE html>
<html lang="en">
<head>
<meta charset="utf-8">
<title>Keelwave Marine – Business Card</title>
<link href="https://fonts.googleapis.com/css2?family=Ubuntu:wght@400;500;700&display=swap" rel="stylesheet">
<style>
  :root {
    --backdrop: #000000;
    --card-blue: #22aae2;
    --card-white: #ffffff;
    --ink-dark: #0b2a44;
    --ink-grey: #4a4a4a;
    --brand-light: #1fa3dd;
    --ring-red: #ec2c5a;
    --ring-dark: #2b2b2f;
    --ring-blue: #1585cf;
    --ring-orange: #f59a23;
    --photo-tone: #cfcfcf;
    --tile-grey: #9b9b9b;
    --tile-blue: #1fa8e0;
    --tile-green: #4cb848;
    --tile-orange: #f6a921;
  }
  * { margin: 0; padding: 0; box-sizing: border-box; }
  html, body { width: 1118px; height: 1200px; overflow: hidden; background: var(--backdrop); }
  body { position: relative; font-family: "Ubuntu", sans-serif; }

  .card { position: absolute; left: 240px; width: 650px; height: 430px; border-radius: 30px; overflow: hidden; }
  .card--front { top: 141px; background: var(--card-blue); color: #fff; }
  .card--back { top: 621px; background: var(--card-white); }

  .social-badge { position: absolute; left: 527px; top: 43px; display: flex; align-items: center; gap: 6px; font-size: 11px; line-height: 1.05; }
  .social-badge__square { width: 24px; height: 24px; background: #fff; border-radius: 3px; }
  .social-badge__label strong { display: block; font-weight: 700; }

  .portrait { position: absolute; left: 207px; top: 37px; width: 236px; height: 236px; }
  .portrait svg { width: 100%; height: 100%; }

  .identity { position: absolute; top: 301px; left: 0; width: 100%; display: flex; justify-content: center; align-items: center; }
  .identity__name { font-weight: 700; font-size: 24px; padding-right: 16px; }
  .identity__role { font-weight: 400; font-size: 20px; padding-left: 16px; border-left: 2px solid #1479b8; line-height: 30px; }

  .services { position: absolute; top: 388px; left: 0; width: 100%; display: flex; justify-content: center; gap: 16px; list-style: none; font-size: 16.5px; }
  .services li::before { content: ""; display: inline-block; width: 4px; height: 4px; background: #fff; margin-right: 6px; vertical-align: middle; }

  .brand { position: absolute; left: 44px; top: 192px; width: 212px; }
  .brand__name { font-weight: 700; font-size: 23px; line-height: 1.2; color: var(--ink-dark); letter-spacing: -0.3px; white-space: nowrap; }
  .brand__tagline { font-weight: 500; font-size: 14px; color: var(--brand-light); margin-top: 12px; letter-spacing: 0.2px; white-space: nowrap; }

  .divider { position: absolute; left: 271px; top: 47px; width: 4px; height: 337px; background: linear-gradient(to bottom, rgba(0,0,0,0), rgba(0,0,0,0.28) 50%, rgba(0,0,0,0)); filter: blur(1.5px); }

  .contacts { position: absolute; left: 273px; top: 117px; list-style: none; }
  .contacts li { display: flex; align-items: center; height: 48.5px; }
  .contacts__tile { width: 58px; height: 48.5px; display: flex; align-items: center; justify-content: center; }
  .contacts__tile svg { width: 30px; height: 30px; }
  .contacts__tile--phone { background: var(--tile-grey); }
  .contacts__tile--chat { background: var(--tile-blue); }
  .contacts__tile--mail { background: var(--tile-green); }
  .contacts__tile--web { background: var(--tile-orange); }
  .contacts__text { padding-left: 14px; font-size: 17px; color: var(--ink-grey); white-space: nowrap; }
</style>
</head>
<body>
  <section class="card card--front">
    <div class="social-badge">
      <span class="social-badge__square"></span>
      <span class="social-badge__label">Find me on<strong>Netlink</strong></span>
    </div>

    <div class="portrait">
      <svg viewBox="0 0 236 236">
        <circle cx="120" cy="122" r="112" fill="rgba(0,0,0,0.18)"/>
        <path d="M118 4 A114 114 0 0 0 4 118" fill="none" stroke="var(--ring-red)" stroke-width="6"/>
        <path d="M118 4 A114 114 0 0 1 232 118" fill="none" stroke="var(--ring-dark)" stroke-width="6"/>
        <path d="M232 118 A114 114 0 0 1 118 232" fill="none" stroke="var(--ring-blue)" stroke-width="6"/>
        <path d="M118 232 A114 114 0 0 1 4 118" fill="none" stroke="var(--ring-orange)" stroke-width="6"/>
        <circle cx="118" cy="118" r="111" fill="#ffffff"/>
        <circle cx="118" cy="118" r="105" fill="var(--photo-tone)" role="img" aria-label="Portrait photo of the regional manager"/>
      </svg>
    </div>

    <div class="identity">
      <span class="identity__name">Rory Calder</span>
      <span class="identity__role">Regional Manager</span>
    </div>

    <ul class="services">
      <li>Environmental</li>
      <li>Medical</li>
      <li>Navigation</li>
      <li>Safety</li>
    </ul>
  </section>

  <section class="card card--back">
    <div class="brand">
      <div class="brand__name">Keelwave Marine</div>
      <div class="brand__tagline">Innovative Ship Solutions</div>
    </div>

    <div class="divider"></div>

    <ul class="contacts">
      <li>
        <span class="contacts__tile contacts__tile--phone">
          <svg viewBox="0 0 30 30" fill="none" stroke="#fff" stroke-width="1.6">
            <rect x="6" y="3" width="12" height="24" rx="2"/>
            <line x1="6" y1="7" x2="18" y2="7"/><line x1="6" y1="22" x2="18" y2="22"/>
            <path d="M21 11 q3 4 0 8 M24 9 q5 6 0 12"/>
          </svg>
        </span>
        <span class="contacts__text">+44 (0) 7700 900418</span>
      </li>
      <li>
        <span class="contacts__tile contacts__tile--chat">
          <svg viewBox="0 0 30 30"><circle cx="15" cy="15" r="10" fill="#0b6fc2" stroke="#fff" stroke-width="1.6"/></svg>
        </span>
        <span class="contacts__text">rory.calder27</span>
      </li>
      <li>
        <span class="contacts__tile contacts__tile--mail">
          <svg viewBox="0 0 30 30" fill="none" stroke="#fff" stroke-width="1.6">
            <path d="M4 12 L15 4 L26 12 V26 H4 Z"/>
            <path d="M4 12 L15 20 L26 12"/>
            <path d="M4 26 L12 18 M26 26 L18 18"/>
          </svg>
        </span>
        <span class="contacts__text">rory.calder@keelwave-marine.com</span>
      </li>
      <li>
        <span class="contacts__tile contacts__tile--web">
          <svg viewBox="0 0 30 30" fill="none" stroke="#fff" stroke-width="1.6">
            <circle cx="15" cy="15" r="11"/>
            <ellipse cx="15" cy="15" rx="5" ry="11"/>
            <line x1="4" y1="15" x2="26" y2="15"/>
            <path d="M6 9 H24 M6 21 H24"/>
          </svg>
        </span>
        <span class="contacts__text">www.keelwave-marine.com</span>
      </li>
    </ul>
  </section>
</body>
</html>
```